No Credit Score QT and ZMR

I'm looking for a banner to display on emails as well as facebook. The facebook banner would need to be square and the other size is 728 x 90. We are a mortgage company that does mostly Military home loans. We would like to start out with just this banner, then do about 20 others once we find the right designer. I need something simple but that stands out. Our company website is www.harborpeakfinancial.com. The text for this will be ( Ask about our "No Credit Score" program for ZMR and QT)

```html
<!DOCTYPE html>
<html lang="en">
<head>
<meta charset="utf-8">
<title>Harbor Peak Financial – No Credit Score Program</title>
<link href="https://fonts.googleapis.com/css2?family=Open+Sans:wght@600;700&display=swap" rel="stylesheet">
<style>
  :root {
    --paper: #ffffff;
    --ink: #1c1c1c;
    --brand-ink: #2b2b2b;
    --accent-green: #1fa637;
    --swoosh-green: #39b54a;
    --cta-orange: #f26a21;
    --cta-text: #ffffff;
    --photo-olive: #8a8a6e;
    --photo-sage: #b9bca4;
    --photo-shadow: #5f6350;
  }
  html, body {
    margin: 0;
    padding: 0;
    overflow: hidden;
    background: var(--paper);
  }
  .banner {
    position: relative;
    width: 1200px;
    height: 148px;
    background: var(--paper);
    overflow: hidden;
    font-family: "Open Sans", Arial, sans-serif;
  }
  .brand {
    position: absolute;
    left: 22px;
    top: 50px;
    display: flex;
    align-items: center;
    gap: 10px;
    color: var(--brand-ink);
    font-weight: 700;
  }
  .brand-mark {
    width: 18px;
    height: 18px;
    background: var(--brand-ink);
  }
  .brand-name {
    display: flex;
    flex-direction: column;
    line-height: 1;
  }
  .brand-name .primary {
    font-size: 27px;
    letter-spacing: 1px;
  }
  .brand-name .secondary {
    font-size: 11px;
    letter-spacing: 6px;
    margin-top: 5px;
  }
  .hero-photo {
    position: absolute;
    left: 270px;
    top: 0;
    width: 330px;
    height: 148px;
  }
  .offer {
    position: absolute;
    left: 624px;
    top: 44px;
    margin: 0;
    font-size: 21px;
    font-weight: 600;
    line-height: 33px;
    color: var(--ink);
  }
  .offer .highlight {
    color: var(--accent-green);
  }
  .cta {
    position: absolute;
    left: 979px;
    top: 49px;
    width: 190px;
    height: 53px;
    background: var(--cta-orange);
    color: var(--cta-text);
    border-radius: 4px;
    display: flex;
    align-items: center;
    justify-content: center;
    font-size: 22px;
    font-weight: 600;
    text-decoration: none;
  }
</style>
</head>
<body>
  <div class="banner">
    <div class="brand">
      <span class="brand-mark"></span>
      <span class="brand-name">
        <span class="primary">HARBOR PEAK</span>
        <span class="secondary">FINANCIAL</span>
      </span>
    </div>

    <svg class="hero-photo" viewBox="0 0 330 148" role="img" aria-label="Photo: soldier in camouflage uniform holding a small model house">
      <defs>
        <linearGradient id="photoTone" x1="0" y1="0" x2="1" y2="1">
          <stop offset="0" stop-color="var(--photo-sage)"/>
          <stop offset="0.55" stop-color="var(--photo-olive)"/>
          <stop offset="1" stop-color="var(--photo-shadow)"/>
        </linearGradient>
      </defs>
      <path d="M60 0 H330 V148 H18 C-6 100 10 40 60 0 Z" fill="url(#photoTone)"/>
      <path d="M48 0 C2 40 -10 100 8 148" fill="none" stroke="var(--swoosh-green)" stroke-width="6"/>
      <path d="M330 0 C318 50 318 100 330 148" fill="none" stroke="var(--paper)" stroke-width="14"/>
    </svg>

    <p class="offer">
      Ask about our "<span class="highlight">No Credit Score</span>"<br>
      program for <span class="highlight">ZMR</span> and <span class="highlight">QT</span>
    </p>

    <a class="cta" href="https://www.harborpeakfinancial.com">Contact Us</a>
  </div>
</body>
</html>
```